Law firm stationary
Letterhead, envelopes, business cards, thank you card, and credit card
Project: Law firm stationary
Law firm stationary - Law
Creative Brief
Use specific fonts
Use what you think works best
Professional
Paul R. Vandemoss
Attorney
27650 East Willowcrest Parkway, Suite 418 Larkfield, Arizona 86999
pvandemoss@qlexhall.net
www.qlexhall.net
I am uploading multiple versions of the logo. Use whatever version you think will work best. This is a new logo that has never been used before, so feel free to revise or modify it if necessary for your design. (1) Letterhead will be standard 8.5" x 11" used in USA. (2) Envelope will be #10 size. It should have return address on the front, in the top left corner. Logo can be there, or on the closing flap. (3) Business card should have something creative on the back, or can be blank if you think that is better. (4) Thank you card should be single sided with measurements: 5.5 inches wide by 4.25 inches tall. (5) Please design an envelope for the thank you card, which will be size A-6 (6.5 inches wide by 4.75 inches high). (6) Please design a credit card. Dimensions will be 3 5/8 inches wide by 2 1/8 inches tall, and room needs to be left for the numbes and expiration date in the usual places. NOTE: This is a sophisticated, business firm. We need to present that image. We DO NOT want graphics like a gavel, scales of justice, or other typical law images. Something more refined is what we are looking for. Thank you!
Be creative, whatever you think is best.

```html
<!DOCTYPE html>
<html lang="en">
<head>
<meta charset="utf-8">
<title>Qlexhall Law Firm stationery</title>
<link href="https://fonts.googleapis.com/css2?family=Libre+Baskerville:wght@400;700&family=Questrial&display=swap" rel="stylesheet">
<style>
:root{
  --red:#b3141c;
  --red-dark:#6e0a10;
  --charcoal:#4a4a4a;
  --grey:#8d8d8d;
  --grey-light:#d8d8d8;
  --paper:#ffffff;
  --stage:#dcd9d5;
  --ink:#2b2b2b;
}
*{box-sizing:border-box;margin:0;padding:0}
html,body{width:1200px;height:899px;overflow:hidden}
body{background:var(--stage);position:relative;font-family:"Questrial",sans-serif;color:var(--ink)}
.piece{position:absolute;background:var(--paper);box-shadow:0 3px 10px rgba(0,0,0,.25);overflow:hidden}

/* firm name lockup */
.firm{display:flex;align-items:center;gap:8px}
.firm-mark{width:22px;height:22px;background:var(--red);flex:none}
.firm-name{font-family:"Libre Baskerville",serif;font-weight:700;color:var(--red);line-height:1.05;letter-spacing:.5px;white-space:nowrap}
.tagline{font-family:"Questrial",sans-serif;color:var(--charcoal);white-space:nowrap}
.web-bar{position:absolute;left:0;right:0;bottom:0;height:12px;background:var(--charcoal);color:#fff;font-size:6px;text-align:right;padding-right:10px;line-height:12px;letter-spacing:1px}
.web-bar::before{content:"";position:absolute;left:0;right:0;top:-3px;height:3px;background:var(--red)}

/* small business cards */
.card-sm{width:218px;height:118px}
.card-front{left:20px;top:40px}
.card-front .firm{position:absolute;left:12px;top:12px}
.card-front .firm-name{font-size:13px}
.card-front .tagline{position:absolute;left:12px;top:44px;font-size:6.5px}
.card-front .holder{position:absolute;left:12px;top:64px}
.holder-name{font-family:"Libre Baskerville",serif;font-size:8px;font-weight:700}
.holder-title{font-size:6px;color:var(--grey)}
.card-front .contact{position:absolute;left:108px;top:62px;font-size:5.5px;line-height:1.45;color:var(--charcoal)}
.card-back-red{left:20px;top:174px;background:linear-gradient(180deg,var(--red) 0%,var(--red-dark) 100%)}
.card-back-red .firm{position:absolute;left:14px;top:26px}
.card-back-red .firm-mark{background:#fff}
.card-back-red .firm-name{color:#fff;font-size:15px}
.card-back-red .tagline{position:absolute;left:14px;top:68px;color:#fff;font-size:7px}
.card-back-white{left:20px;top:296px}
.card-back-white .firm{position:absolute;left:16px;top:24px}
.card-back-white .firm-name{font-size:15px}
.card-back-white .tagline{position:absolute;left:16px;top:66px;font-size:7px}

/* large card */
.card-lg-under{position:absolute;left:292px;top:72px;width:320px;height:380px;background:var(--grey);box-shadow:0 3px 10px rgba(0,0,0,.25)}
.card-lg{left:258px;top:42px;width:320px;height:410px}
.card-lg .firm{position:absolute;left:30px;top:40px}
.card-lg .firm-mark{width:34px;height:34px}
.card-lg .firm-name{font-size:22px}
.card-lg .tagline{position:absolute;left:30px;top:94px;font-size:10px}
.rule{position:absolute;left:0;height:4px;background:var(--red)}
.card-lg .rule{top:118px;width:240px}
.card-lg .holder{position:absolute;left:30px;top:175px;text-align:left}
.card-lg .holder-name{font-size:17px;font-weight:400}
.card-lg .holder-title{font-size:12px;color:var(--charcoal);margin-top:6px}
.card-lg .rule.low{top:240px;width:320px;height:2px;background:var(--grey-light)}
.card-lg .contact{position:absolute;left:30px;top:262px;font-family:"Libre Baskerville",serif;font-size:10.5px;line-height:1.55}
.card-lg .web-bar{height:16px;font-size:8px;line-height:16px}

/* letterhead */
.letterhead{left:627px;top:12px;width:556px;height:718px}
.letterhead .firm{position:absolute;left:36px;top:28px}
.letterhead .firm-mark{width:30px;height:30px}
.letterhead .firm-name{font-size:21px}
.letterhead .tagline{position:absolute;left:36px;top:80px;font-size:9px}
.letterhead .sender{position:absolute;left:300px;top:26px;font-size:7px;line-height:1.45;color:var(--charcoal)}
.letterhead .sender.phones{left:450px}
.letterhead .rule{top:98px;width:556px;height:2px;background:var(--grey-light)}
.letter-body{position:absolute;left:36px;right:36px;top:124px;font-size:9.5px;line-height:1.55;color:var(--ink)}
.letter-body p{margin-bottom:14px}
.letterhead .web-bar{height:16px;line-height:16px;font-size:8px}

/* envelopes */
.env{position:absolute;box-shadow:0 3px 10px rgba(0,0,0,.25)}
.env svg{display:block}
.env-open{left:36px;top:462px;width:390px;height:224px}
.env-red{left:219px;top:630px;width:392px;height:196px}
.env-grey{left:486px;top:585px;width:292px;height:194px}
.env-small{left:705px;top:680px;width:268px;height:158px;background:var(--paper)}
.env-small .firm{position:absolute;left:14px;top:14px}
.env-small .firm-mark{width:14px;height:14px}
.env-small .firm-name{font-size:10px}
.env-small .return{position:absolute;left:14px;top:44px;font-size:5.5px;line-height:1.45;color:var(--charcoal)}
.env-small .web-bar{height:9px;line-height:9px;font-size:5px}
</style>
</head>
<body>

<!-- business card front -->
<section class="piece card-sm card-front">
  <div class="firm"><span class="firm-mark"></span><span class="firm-name">Qlexhall<br>Law Firm, PC</span></div>
  <p class="tagline">Thoughtful Counsel for Demanding Matters</p>
  <div class="holder"><p class="holder-name">Paul R. Vandemoss</p><p class="holder-title">Attorney</p></div>
  <p class="contact">27650 East Willowcrest Parkway<br>Suite 418<br>Larkfield, Arizona 86999<br>(602) 555-0148<br>pvandemoss@qlexhall.net</p>
  <div class="web-bar">www.qlexhall.net</div>
</section>

<!-- business card back, red -->
<section class="piece card-sm card-back-red">
  <div class="firm"><span class="firm-mark"></span><span class="firm-name">Qlexhall<br>Law Firm, PC</span></div>
  <p class="tagline">Thoughtful Counsel for Demanding Matters</p>
</section>

<!-- business card back, white -->
<section class="piece card-sm card-back-white">
  <div class="firm"><span class="firm-mark"></span><span class="firm-name">Qlexhall<br>Law Firm, PC</span></div>
  <p class="tagline">Thoughtful Counsel for Demanding Matters</p>
  <div class="web-bar">www.qlexhall.net</div>
</section>

<!-- large vertical card -->
<div class="card-lg-under"></div>
<section class="piece card-lg">
  <div class="firm"><span class="firm-mark"></span><span class="firm-name">Qlexhall<br>Law Firm, PC</span></div>
  <p class="tagline">Thoughtful Counsel for Demanding Matters</p>
  <div class="rule"></div>
  <div class="holder"><p class="holder-name">Paul R. Vandemoss</p><p class="holder-title">Attorney</p></div>
  <div class="rule low"></div>
  <p class="contact">27650 East Willowcrest Parkway<br>Suite 418<br>Larkfield, Arizona 86999<br><br>t: (602) 555-0148<br>f: (480) 555-0193<br>e: pvandemoss@qlexhall.net</p>
  <div class="web-bar">www.qlexhall.net</div>
</section>

<!-- letterhead -->
<section class="piece letterhead">
  <div class="firm"><span class="firm-mark"></span><span class="firm-name">Qlexhall<br>Law Firm, PC</span></div>
  <p class="tagline">Thoughtful Counsel for Demanding Matters</p>
  <p class="sender">27650 East Willowcrest Parkway<br>Suite 418<br>Larkfield, Arizona 86999</p>
  <p class="sender phones">t: (602) 555-0148<br>f: (480) 555-0193<br>www.qlexhall.net</p>
  <div class="rule"></div>
  <div class="letter-body">
    <p>Lorem Ipsum is simply dummy text of the printing and typesetting industry. Lorem Ipsum has been the industry's standard dummy text ever since the 1500s, when an unknown printer took a galley of type and scrambled it to make a type specimen book. It has survived not only five centuries, but also the leap into electronic typesetting, remaining essentially unchanged. It was popularised in the 1960s with the release of Letraset sheets containing Lorem Ipsum passages, and more recently with desktop publishing software like Aldus PageMaker including versions of Lorem Ipsum.</p>
    <p>Contrary to popular belief, Lorem Ipsum is not simply random text. It has roots in a piece of classical Latin literature from 45 BC, making it over 2000 years old. A Latin professor at a small college in Virginia looked up one of the more obscure Latin words, consectetur, from a Lorem Ipsum passage, and going through the cites of the word in classical literature, discovered the undoubtable source. Lorem Ipsum comes from sections 1.10.32 and 1.10.33 of "de Finibus Bonorum et Malorum" (The Extremes of Good and Evil) by Cicero, written in 45 BC. This book is a treatise on the theory of ethics, very popular during the Renaissance. The first line of Lorem Ipsum, "Lorem ipsum dolor sit amet..", comes from a line in section 1.10.32.</p>
  </div>
  <div class="web-bar">www.qlexhall.net</div>
</section>

<!-- #10 envelope, back with open flap -->
<div class="env env-open">
  <svg width="390" height="224" viewBox="0 0 390 224">
    <rect x="0" y="70" width="390" height="154" fill="#f2f2f2"/>
    <polygon points="0,70 195,0 390,70" fill="#ffffff"/>
    <polygon points="0,224 195,140 390,224" fill="#e6e6e6"/>
    <polygon points="0,70 0,224 170,150" fill="#ececec"/>
    <polygon points="390,70 390,224 220,150" fill="#ececec"/>
    <rect x="180" y="34" width="30" height="30" fill="#b3141c"/>
  </svg>
</div>

<!-- #10 envelope, back with red flap -->
<div class="env env-red">
  <svg width="392" height="196" viewBox="0 0 392 196">
    <rect x="0" y="0" width="392" height="196" fill="#f4f4f4"/>
    <polygon points="0,196 196,110 392,196" fill="#e4e4e4"/>
    <polygon points="0,0 196,120 392,0" fill="#8c0f15"/>
    <polygon points="0,0 196,100 392,0" fill="#b3141c"/>
    <rect x="184" y="30" width="24" height="24" fill="#ffffff"/>
  </svg>
</div>

<!-- A-6 envelope, grey flap -->
<div class="env env-grey">
  <svg width="292" height="194" viewBox="0 0 292 194">
    <rect x="0" y="0" width="292" height="194" fill="#f4f4f4"/>
    <polygon points="0,194 146,110 292,194" fill="#e4e4e4"/>
    <polygon points="0,0 146,108 292,0" fill="#4a4a4a"/>
    <rect x="136" y="26" width="20" height="20" fill="#ffffff"/>
  </svg>
</div>

<!-- A-6 envelope, front -->
<section class="env env-small">
  <div class="firm"><span class="firm-mark"></span><span class="firm-name">Qlexhall Law Firm, PC</span></div>
  <p class="return">27650 East Willowcrest Parkway<br>Suite 418<br>Larkfield, Arizona 86999</p>
  <div class="web-bar">www.qlexhall.net</div>
</section>

</body>
</html>
```